Business Card Design - Law Firm

I need a business card design. I have attached a picture of the law firm's website and logo. The business card design should be consistent with those pictures. There should be a place for the employee name, employee job title, telephone number, facsimile number, address, website url, and email address for each employee.
Industry/Entity Type
Business

```html
<!DOCTYPE html>
<html lang="en">
<head>
<meta charset="utf-8">
<title>Calloway Law – Business Cards</title>
<link rel="stylesheet" href="https://fonts.googleapis.com/css2?family=Cormorant+Garamond:wght@500&family=Tinos&display=swap">
<style>
  :root {
    --backdrop: #4a4a4a;
    --card-dark: #1c1c1c;
    --card-light: #ffffff;
    --gold: #b39b4f;
    --ink: #1a1a1a;
    --paper-text: #f1f1f1;
    --faint-mark: rgba(255,255,255,0.05);
  }
  * { margin: 0; padding: 0; box-sizing: border-box; }
  html, body { width: 1200px; height: 960px; overflow: hidden; }
  body {
    position: relative;
    background: var(--backdrop);
    font-family: "Tinos", "Times New Roman", serif;
  }
  .card {
    position: absolute;
    width: 548px;
    height: 316px;
    box-shadow: 3px 4px 6px rgba(0,0,0,0.45);
    overflow: hidden;
  }
  .card--front { left: 324px; top: 103px; background: var(--card-dark); }
  .card--back-dark { left: 24px; top: 525px; background: var(--card-dark); }
  .card--back-light { left: 613px; top: 525px; background: var(--card-light); }

  .front-band {
    position: absolute; left: 0; top: 0;
    width: 100%; height: 129px;
    background: var(--card-light);
  }

  .brand {
    position: absolute;
    display: flex;
    align-items: center;
    gap: 12px;
    white-space: nowrap;
  }
  .brand__square {
    width: 34px; height: 34px;
    background: var(--ink);
  }
  .card--back-dark .brand__square { background: #2a2a2a; border: 1px solid #3a3a3a; }
  .brand__name {
    font-family: "Cormorant Garamond", Georgia, serif;
    font-weight: 500;
    font-size: 30px;
    letter-spacing: 1px;
    color: var(--gold);
  }
  .front-band .brand { left: 184px; top: 44px; }
  .card--back-dark .brand,
  .card--back-light .brand { left: 50%; top: 137px; transform: translateX(-50%); }

  .employee { position: absolute; left: 63px; top: 166px; }
  .employee__name { font-size: 19px; color: var(--gold); line-height: 1.1; }
  .employee__title { font-size: 15px; color: var(--paper-text); line-height: 1.2; }

  .front-mark {
    position: absolute; left: 72px; top: 243px;
    width: 50px; height: 50px;
    background: var(--faint-mark);
  }

  .contact {
    position: absolute; left: 319px; top: 191px;
    list-style: none;
    font-size: 15px;
    line-height: 18px;
    color: var(--gold);
    white-space: nowrap;
  }
  .contact__label { color: var(--paper-text); }
  .contact__address { color: var(--paper-text); }

  .web {
    position: absolute; left: 0; right: 0; top: 287px;
    text-align: center;
    font-size: 15px;
  }
  .card--back-dark .web { color: var(--gold); }
  .card--back-light .web { color: var(--ink); }
</style>
</head>
<body>

<section class="card card--front" aria-label="Card front">
  <div class="front-band">
    <div class="brand">
      <span class="brand__square"></span>
      <span class="brand__name">Calloway Law</span>
    </div>
  </div>
  <div class="employee">
    <p class="employee__name">Morgan Ellis</p>
    <p class="employee__title">Attorney at law</p>
  </div>
  <div class="front-mark" aria-hidden="true"></div>
  <ul class="contact">
    <li class="contact__address">12 Elm Court, Suite 4</li>
    <li><span class="contact__label">Tel:</span> +00&nbsp; 4820 1736</li>
    <li><span class="contact__label">Fax:</span> +00&nbsp; 4820 1737</li>
    <li>morgan@callowaylaw.com</li>
    <li>www.callowaylaw.com</li>
  </ul>
</section>

<section class="card card--back-dark" aria-label="Card back, dark">
  <div class="brand">
    <span class="brand__square"></span>
    <span class="brand__name">Calloway Law</span>
  </div>
  <p class="web">www.callowaylaw.com</p>
</section>

<section class="card card--back-light" aria-label="Card back, light">
  <div class="brand">
    <span class="brand__square"></span>
    <span class="brand__name">Calloway Law</span>
  </div>
  <p class="web">www.callowaylaw.com</p>
</section>

</body>
</html>
```